Quorvane - corporate Business Card

We need a good look and innovative business card for a new start up company based in Los Angeles called "Quorvane". We are in a payment business, including payment card, app, and ewallet. We are expert in online payment and Card not present (CNP) transaction.
We need an innovative, modern business card.

Our logo font is Aero Matics

Target Market(s)

Startup - Bank - Online Payment - Card Manufacturing

Industry/Entity Type

Startup

Contact Information for Business Card

phone: 424 555 0173 - Address: 4270 Marbrook blvd, Ashvale City, CA 90418

Requirements
Must have
• Message: innovative, professional, expert, high tech, trust, online payment expert, security
Nice to have
• no comment
Should not have
• no Comment

```html
<!DOCTYPE html>
<html lang="en">
<head>
<meta charset="utf-8">
<title>Quorvane — Business Card</title>
<link rel="stylesheet" href="https://fonts.googleapis.com/css2?family=Saira+Condensed:wght@500;600&display=swap">
<style>
  :root {
    --brand-red: #b71d2e;
    --ink: #111111;
    --paper: #ffffff;
  }
  html, body {
    margin: 0;
    padding: 0;
    overflow: hidden;
    background: var(--paper);
  }
  .card {
    position: relative;
    width: 1200px;
    height: 721px;
    background: var(--paper);
    overflow: hidden;
    font-family: "Saira Condensed", "Arial Narrow", sans-serif;
  }
  .brand-dot {
    position: absolute;
    left: 220px;
    top: 142px;
    width: 188px;
    height: 188px;
    border-radius: 50%;
    background: var(--brand-red);
  }
  .brand-name {
    position: absolute;
    left: 40px;
    width: 528px;
    top: 352px;
    margin: 0;
    text-align: center;
    font-weight: 600;
    font-size: 118px;
    line-height: 1;
    letter-spacing: 2px;
    color: var(--brand-red);
  }
  .divider {
    position: absolute;
    left: 597px;
    top: 96px;
    width: 15px;
    height: 528px;
    background: linear-gradient(to bottom,
      rgba(183, 29, 46, 0) 0%,
      var(--brand-red) 45%,
      var(--brand-red) 55%,
      rgba(183, 29, 46, 0) 100%);
  }
  .contact-item {
    position: absolute;
    left: 686px;
    display: flex;
    align-items: flex-start;
  }
  .contact-item svg {
    flex: none;
    fill: var(--brand-red);
  }
  .contact-text {
    margin: 0;
    font-weight: 500;
    font-size: 37px;
    line-height: 46px;
    color: var(--ink);
    letter-spacing: 0.3px;
  }
  .contact-address { top: 248px; }
  .contact-address svg { margin: 18px 28px 0 2px; }
  .contact-phone { top: 416px; }
  .contact-phone svg { margin: -4px 14px 0 0; }
  .contact-phone .contact-text { word-spacing: 8px; }
</style>
</head>
<body>
  <main class="card">
    <div class="brand-dot" aria-hidden="true"></div>
    <h1 class="brand-name">Quorvane</h1>

    <div class="divider" aria-hidden="true"></div>

    <div class="contact-item contact-address">
      <svg width="42" height="66" viewBox="0 0 42 66" aria-hidden="true">
        <path d="M21 0C9.4 0 0 9.2 0 20.6c0 10.8 12.5 29.6 21 45.4 8.5-15.8 21-34.6 21-45.4C42 9.2 32.6 0 21 0zm0 29.5a9 9 0 1 1 0-18 9 9 0 0 1 0 18z" fill-rule="evenodd"/>
      </svg>
      <p class="contact-text">4270 Marbrook blvd,<br>Ashvale City, CA 90418</p>
    </div>

    <div class="contact-item contact-phone">
      <svg width="56" height="42" viewBox="0 0 56 42" aria-hidden="true">
        <path d="M2 12C6 3 18 0 28 0s22 3 26 12l-1 5-10 1-2-6c-4-2-9-2-13-2s-9 0-13 2l-2 6-10-1z"/>
        <path d="M18 10h20v6l10 10 2 16H6l2-16 10-10z"/>
        <g fill="#fff">
          <rect x="18" y="21" width="4" height="3"/><rect x="26" y="21" width="4" height="3"/><rect x="34" y="21" width="4" height="3"/>
          <rect x="18" y="27" width="4" height="3"/><rect x="26" y="27" width="4" height="3"/><rect x="34" y="27" width="4" height="3"/>
          <rect x="18" y="33" width="4" height="3"/><rect x="26" y="33" width="4" height="3"/><rect x="34" y="33" width="4" height="3"/>
        </g>
      </svg>
      <p class="contact-text">424 555 0173</p>
    </div>
  </main>
</body>
</html>
```